Vehicle Service Contract Brochure

https://vidloop.tv/Qm7zXh2LpaW <- WATCH BEFORE STARTING
Feedback on current designs (generally):
https://vidloop.tv/Tr4kWn8BveJ

Finally (from the google doc):UPDATE 10/16/24
The below document is *The Vehicle Service Contract* we need to TURN THIS DOCUMENT into a visual display of customer benefits - use enough panels or pages to display the CUSTOMER BENEFITS in a visually appealing and persuasive way, while displaying the *Vehicle Service Contract* in its entirety, independent of the customer benefits (back pages).

Design a vehicle service contract brochure that car dealerships can present to their customers.

Create a two sided multiple panel brochure:
Audience 1 - Car Buyers
Audience 2 – Car Dealership Sales Person. He / She will use brochure to point out main selling points & differentiators
Audience 3 – Mechanics – they will use this brochure to understand how to file a claim

Main content (customer benefits) for brochure can be found here, Pages 1-9:

https://papershelf.net/doc/9302Kx8Pqe5Lwz3Vtn0bYhsaRjmfC/edit?usp=sharing&ouid=560291837465019283746&rtpof=true&sd=true

Use KT_Example as main guide for content areas / design style.

Use Vesta Shield 1 (page2) as effective example of displaying a high volume of covered items

Our website is mobqen.com
Updates

Please watch before starting:

Need extra days to review

Target Market(s)

Used Car buyers

Industry/Entity Type

Automotive Repair

Colors

Designer to choose colors to be used in the design.

Requirements
Must have
• QR Codes Pointing to Website
Nice to have
• Icons and infographics
Should not have
• Too much fine print

```html
<!DOCTYPE html>
<html lang="en">
<head>
<meta charset="utf-8">
<title>Vehicle Service Contract – Plan Details</title>
<link href="https://fonts.googleapis.com/css2?family=Arimo:wght@400;700&display=swap" rel="stylesheet">
<style>
  :root{
    --page-bg:#e1e1e1;
    --panel:#231f20;
    --ink:#ffffff;
    --accent:#0e8fdc;
    --logo-bg:#ffffff;
    --logo-ink:#1d1d1d;
  }
  html,body{margin:0;padding:0;width:1200px;height:1200px;overflow:hidden;background:var(--page-bg);}
  body{font-family:"Arimo",Arial,sans-serif;color:var(--ink);position:relative;}
  .sheet{position:absolute;left:4px;top:148px;width:1192px;height:904px;background:var(--panel);overflow:hidden;}
  .column{position:absolute;font-size:9px;line-height:11.2px;text-align:justify;}
  .column p{margin:0;}
  .col-plans{left:21px;top:18px;width:355px;}
  .col-benefits{left:401px;top:17px;width:367px;}
  .col-exclusions{left:795px;top:13px;width:390px;}
  .section-title{font-size:15px;line-height:16.5px;font-weight:700;text-transform:uppercase;margin:0;letter-spacing:.1px;text-align:left;}
  .section-title.spread{text-align:justify;text-align-last:left;letter-spacing:1.4px;}
  .section{margin-bottom:13px;}
  .sub-title{font-weight:700;}
  .gap{height:11px;}
  .parts-title{font-size:13px;line-height:15px;font-weight:700;margin:0;}
  .dot{position:absolute;width:9px;height:9px;border-radius:50%;background:var(--accent);}
  .brand-block{position:absolute;left:799px;top:961px;width:397px;height:75px;background:var(--logo-bg);display:flex;align-items:center;justify-content:center;gap:10px;}
  .brand-name{font-family:"Arimo",Arial,sans-serif;font-weight:700;font-size:20px;color:var(--logo-ink);letter-spacing:.3px;}
  .brand-mark{width:14px;height:14px;border-radius:50%;background:var(--logo-ink);}
</style>
</head>
<body>
<div class="sheet">
  <div class="column col-plans">
    <div class="section">
      <h2 class="section-title">Plan Name: Beyond Essential</h2>
      <p>Includes all the benefits of the ESSENTIAL DIAGNOSIS AND BREAKDOWN plan plus the benefits listed below</p>
      <p>Plan Specific Benefit Limit: $2500</p>
    </div>
    <div class="section">
      <h2 class="section-title">Basic Maintenance</h2>
      <p>We will reimburse You for up to (4) verified oil changes per contract year, limited to the time and mileage frequency recommended by the manufacturer.</p>
      <p>Each oil change reimbursement is limited to $50.00.</p>
      <p>You'll be required to provide receipts for the oil change.</p>
      <p>We do not reimburse for DIY oil changes or DIY oil change supplies &amp; fluids.</p>
      <p>You'll need to provide documentation to verify the oil change occurred on a covered vehicle. Reimbursement requests must be submitted within 7 days of service and can be made online at mobqen.com/oilchange</p>
    </div>
    <div class="section">
      <h2 class="section-title spread">Tire &amp; Wheel Road Hazard Repair / Replacement</h2>
      <p>We will reimburse You for tire and wheel repairs that become functionally necessary due to impact with road hazards.</p>
      <p>In order to access this benefit we require evidence of vehicles condition at time of sale through mobqen.com/register.</p>
      <p>If the tread on Your Covered Tire is worn down to 3/32" (by the tread wear indicator), the Covered Tire will be considered worn out and will no longer be eligible for Coverage under this Contract regardless of the age of the tire.</p>
      <p>You will be required to provide proof of failure &amp; evidence of road hazard impact.</p>
      <p>Limited to $150.00 per tire and $200.00 per wheel.</p>
      <p>Maximum (4) tires &amp; (4) wheels during the contract term.</p>
      <p>Reimbursement requests must be submitted within 7 days of service and can be made online at mobqen.com/roadhazard</p>
    </div>
    <div class="section">
      <h2 class="section-title">Cosmetic Wheel Repair</h2>
      <p>We will reimburse you for cosmetic repairs of Covered Wheels such as nicks, scrapes and curb rash resulting from damage by a Road Hazard or due to contact with medians, curbs, parking stops or other hazards</p>
      <p>In order to access this benefit we require evidence of vehicles condition at time of sale through mobqen.com/register</p>
      <p>Coverage applies only to wheels installed on vehicle at the time of sale</p>
      <p>$100 per cosmetic repair &amp; 4 repairs per contract.</p>
      <p>Reimbursement requests must be submitted within 7 days of service and can be made online at mobqen.com/cosmeticwheel</p>
    </div>
    <div class="section">
      <h2 class="section-title">Paintless Dent Repair</h2>
      <p>We will reimburse you for paintless dent repairs resulting from normal vehicle wear and tear, including but not limited to door dings.</p>
      <p>Paintless dent repair removes small dents and dings without harming the factory's original finish.</p>
      <p>In order to access this benefit we require evidence of vehicles condition at time of sale through mobqen.com/register</p>
      <p>Exterior vertical painted sheet metal body panels only</p>
      <p>Dent or ding not to exceed 4 inches in diameter</p>
      <p>Limited to $100 per repair &amp; 4 repairs per contract.</p>
      <p>Reimbursement requests must be submitted within 7 days of service and can be made online at mobqen.com/paintlessdent</p>
    </div>
    <div class="section">
      <h2 class="section-title">Plan Name: Industry Best</h2>
      <p>Includes all the benefits of the ESSENTIAL DIAGNOSIS AND BREAKDOWN plan + BEYOND ESSENTIAL plan</p>
      <p>Plan Specific Benefit Limit: $5,000</p>
    </div>
    <div class="section">
      <h2 class="section-title">Dissapearing Deductible</h2>
      <p>Where applicable, your deductible will be waived when you return to the seller's repair facility for DIAGNOSIS AND BREAKDOWN plan repairs</p>
    </div>
    <div class="section">
      <h2 class="section-title">Enhanced Maintenance</h2>
      <p class="sub-title">Major Service</p>
      <p>We will reimburse you up to $500.00 for (1) major odometer manufacturer recommended service during the term of your contract.</p>
      <p class="sub-title">Oil Changes</p>
      <p>We will reimburse You for up to (4) verified oil changes per contract year, limited to the time and mileage frequency recommended by the manufacturer.</p>
    </div>
  </div>

  <div class="column col-benefits">
    <p>Each oil change reimbursement is limited to $75.00.</p>
    <p>We do not reimburse for DIY oil changes or DIY oil change supplies &amp; fluids.</p>
    <p>Reimbursement requests must be submitted, along with receipt, within 7 days of service and can be made online at mobqen.com/oilchange</p>
    <p class="sub-title">KEY REPLACEMENT</p>
    <p>In the event your key fob becomes inoperable, we will reimburse you up to $250.00 for the verified purchase of an OEM replacement key fob.</p>
    <p>Limit (1) Key Fob Replacement per contract term</p>
    <p>In order to access this benefit we require evidence of working key fob at time of sale through mobqen.com/register</p>
    <p>Reimbursement requests must be submitted, along with proof of failure and purchase receipt, within 7 days of service and can be made online at mobqen.com/keyfob</p>
    <div class="gap"></div>
    <p class="sub-title">THEFT PROTECTION PROGRAM</p>
    <p>A Theft Protection Program &amp; Alphanumeric Registration Code will be provided by seller.</p>
    <p>Program must be installed in clear view on the front driver's side window.</p>
    <div class="gap"></div>
    <h2 class="section-title">Theft Total Loss Benefit</h2>
    <p>In the event the Theft Protection Program fails to prevent the Covered Vehicle from being stolen, and further, that the alphanumeric registration code fails to affect recovery of the Covered Vehicle and such failure results in the Covered Vehicle being declared a total loss due to either unrecovered theft or constructive total loss as a direct result of a theft, we will pay you the lesser of $2500.00 or the vehicles Valora Guide Clean Trade Value the time of loss.</p>
    <p>In order to access this benefit, within 7 days of the total loss declaration, you'll be required to provide:</p>
    <p>Police report confirming the theft</p>
    <p>Insurance company documentation confirming total loss</p>
    <p>Documentation to be provided at mobqen.com/lossbenefit</p>
    <p>COLLISION TOTAL LOSS BENEFIT In the event that during the contract term, an insurance company deems your vehicle a total loss as the result of a collision with another vehicle or due to unintentional impact with road hazards or road obstacles, we will pay you the lesser of $2500.00 or the vehicles Valora Guide Clean Trade Value the time of loss.</p>
    <p>In order to access this benefit, within 7 days of the total loss declaration, you'll be required to provide:</p>
    <p>Police report confirming the unintentional collision</p>
    <p>Insurance company documentation confirming total loss</p>
    <p>Documentation to be provided at mobqen.com/lossbenefit</p>
    <div class="gap"></div><div class="gap"></div>
    <h2 class="section-title">Exclusions – What Is Not Covered</h2>
    <div class="gap"></div>
    <p class="sub-title">Vehicles Not Covered</p>
    <p>This Agreement does NOT provide coverage for any of the following vehicles:</p>
    <p>Vehicles not certified for sale within the United States, vehicles whose Valora Guide value exceeds $100,000.00 at the time this agreement is being purchased, and vehicles that have been sold for scrap. Trucks or vans with a Gross Vehicle Weight (GVW) in excess of 13,300 lbs.</p>
    <p>Vehicles used for construction purposes, commercial towing, commercial farm operation, volunteer public service(s), snow plowing, livery, or any type of emergency vehicle.</p>
    <p>Vehicles used for on or off-road racing</p>
    <p>Vehicles which are equipped or used for towing more than what is recommended by the manufacturer.</p>
    <p>Vehicles with lift kits over 6 inches, drops exceeding 4 inches.</p>
    <div class="gap"></div>
    <p class="sub-title">Conditions Not Covered</p>
    <p>This Agreement does NOT provide coverage under any of the following circumstances or conditions:</p>
    <div class="gap"></div>
    <p>Any repair(s) and/or replacement(s) not authorized by Us prior to the commencement of any repair(s)</p>
    <p>Damage caused by Your failure to take reasonable precautions to prevent damage when an apparent problem exists (e.g., change in engine temperature condition, unusual noises, leaking fluids, shaking, unusual shifting, illuminated warning lights, etc.).</p>
    <p>Repairs required as a result of improper prior repair.</p>
    <p>Loss, damage or expense resulting directly or indirectly from an intentional, dishonest, fraudulent, criminal or illegal act committed by You, Your employee or agent, or occurring due to confiscation or repossession.</p>
    <p>A Breakdown caused by accident, civil commotion or riot, nuclear contamination, collision (including roadbed collision), glass breakage, hail, lightening, malicious mischief, earthquake, explosion, volcanic eruption, falling objects, fire or smoke, flood, freezing, windstorm and other external forces or events.</p>
  </div>

  <div class="column col-exclusions">
    <p>Any loss, damage, or expense normally covered by a standard automobile insurance policy including personal or property liability coverages, comprehensive coverages or uninjured motorist coverages.</p>
    <p>A breakdown caused by use of improper fluids, fluid contamination, fuels containing more than 10% ethanol, Biofuel, gas with lower octane rating than required by the manufacturer, use of motor oil or any other type of lubricant that is not recommended by the manufacturer, oil contamination.</p>
    <p>A Breakdown caused by the lack of proper and necessary amounts of coolants or lubricants, or resulting from carbon, contaminant(s) and contamination of fluids, foreign object(s), rust or corrosion, sludge, salt, or due to leaking fluids, fuels, coolants or lubricants from non-covered parts.</p>
    <p>Breakdown of a Covered Part caused by a non-Covered Part.</p>
    <p>A Breakdown caused by negligence, misuse, improper servicing or failure by You to perform manufacturer required/recommended maintenance services.</p>
    <p>A breakdown caused by use of vehicle outside of normal operational guidelines, including but not limited to:</p>
    <p>Excessive payloads or tow loads</p>
    <p>Racing or reckless driving</p>
    <p>Any repair or replacement of any Covered Part if a Breakdown/Mechanical Breakdown has not occurred.</p>
    <p>Noises</p>
    <p>Gradual reduction in operating performance is not covered unless it exceeds the published tolerances allowed by the manufacturer.</p>
    <p>Valves, valve guides, valve seals, and/or piston rings are not covered if the purpose of such is simply to raise the engine's compression, performance, or to reach acceptable oil consumption.</p>
    <p>A Breakdown of any part if the odometer is inoperative for more than one (1) month or one thousand (1,000) miles or has been tampered with or has been disconnected subsequent to Your purchase of the vehicle.</p>
    <p>A Breakdown or repair occurring outside the United States, its territories and possessions, or Canada.</p>
    <p>Any fees or expenses charged for the disposal, cleanup, neutralization, removal, treatment or detoxification of environmentally unsafe materials.</p>
    <p>Any Pre-Existing condition including any Covered Part that was broken, worn beyond serviceable limits, or making noise at the time of purchase, or any component or system that was not functioning properly upon the first attempt to operate.</p>
    <p>Any Breakdown occurring before Breakdown coverage takes effect.</p>
    <p>If the information provided by You, or the Repair Facility cannot be verified as accurate or is found to be deceptively inaccurate.</p>
    <p>Incidental or consequential damages, except as expressly provided otherwise in this Agreement, including personal injury, physical damage, loss of use, loss of time, storage charges, inconvenience and commercial loss.</p>
    <div class="gap"></div>
    <h3 class="parts-title">Parts Breakdowns, Repairs and Services Not Covered</h3>
    <p>This Agreement does NOT provide coverage for any of the following repairs and/or services:</p>
    <p>Interior adjustments and wear items including but not limited to</p>
    <p>buttons, carpet, water leaks, dash pad, door and window handles, knobs, rearview mirror (glass, housing, housing contents), and trim</p>
    <p>Exterior adjustments and wear items including but not limited to</p>
    <p>glass, bright metal, bumpers, body panels, door handles, latches, hinges, moldings, outside ornamentation, wiper blades, convertible or vinyl tops, paint rust, sheet metal, side-view mirrors (glass, housing, housing contents), air and water leaks, weather-strip, wheel covers/ornaments, wind noise, wheel balancing and alignment, wheel studs, physical damage to alignment, bumper, body parts, sunroof rails and guides</p>
    <p>Mechanical wear items including but not limited to:</p>
    <p>Manual clutch, pressure plate, throw out bearings, clutch master or slave cylinder, manual transmission clutch disc and lining, shock absorbers, spark plugs and wires, tune ups, brakes (drums, shoes, linings, disc rotors and pads)</p>
    <p>Filters, lubricants, coolants, refrigerants, fluids, fuses, relays, hardware, bolts and fasteners, belts, hoses, all lights &amp; light fixtures</p>
    <p>Lead acid battery, failure due to battery loss of capacity, battery cables</p>
    <p>Breakdown of any part which the United States Environmental Protection Agency (EPA) has determined to be emission related, which is included on a current list published by the EPA of such parts, and which is within the EPA time and mileage emissions warranty period, including but not limited to:</p>
    <div class="gap"></div>
    <p class="sub-title">Exhaust Gas Conversion Systems:</p>
    <p>oxygen sensor, thermal reactor, catalytic converter, dual-walled exhaust pipe 2. Exhaust Gas Recirculation System: EGR valve, thermal vacuum switch, EGR solenoid, EGR spacer plate, EGR backpressure transducer, sensor and switches use to control EGR flow</p>
  </div>
</div>

<span class="dot" style="left:13px;top:170px"></span>
<span class="dot" style="left:13px;top:226px"></span>
<span class="dot" style="left:13px;top:328px"></span>
<span class="dot" style="left:13px;top:470px"></span>
<span class="dot" style="left:13px;top:582px"></span>
<span class="dot" style="left:13px;top:697px"></span>
<span class="dot" style="left:13px;top:755px"></span>
<span class="dot" style="left:13px;top:799px"></span>
<span class="dot" style="left:388px;top:167px"></span>
<span class="dot" style="left:388px;top:365px"></span>
<span class="dot" style="left:388px;top:985px"></span>
<span class="dot" style="left:782px;top:311px"></span>
<span class="dot" style="left:782px;top:356px"></span>
<span class="dot" style="left:782px;top:386px"></span>
<span class="dot" style="left:782px;top:421px"></span>
<span class="dot" style="left:782px;top:500px"></span>
<span class="dot" style="left:782px;top:642px"></span>

<div class="brand-block">
  <span class="brand-mark"></span>
  <span class="brand-name">Mobqen Dealer Services</span>
</div>
</body>
</html>
```